Creation of a cover for a book with an image provided. It is mainly a typographical work. PICTURE (Quiet Harbor IV) IS NOW AVAILABLE

Target Market(s)

General Public

Colors

Designer to choose colors to be used in the design.

Requirements
Must have
• Upper edge: "Mireille Fontaz" (author) Title: "Rain before the harvest" Bottom edge: "Marrow Editions"

```html
<!DOCTYPE html>
<html lang="fr">
<head>
<meta charset="utf-8">
<title>Rain before the harvest — Mireille Fontaz</title>
<link rel="stylesheet" href="https://fonts.googleapis.com/css2?family=Anton&family=Roboto+Condensed:wght@300;700&display=swap">
<style>
  :root {
    --ink: #050608;
    --paper: #ffffff;
    --paint-yellow: #e9d21c;
    --paint-green: #3f9a3a;
    --paint-orange: #e0521c;
    --paint-red: #c8241e;
    --paint-blue: #2c4f9c;
    --paint-sky: #8fb9d6;
    --photo-label: #2a2c30;
  }
  html, body {
    margin: 0;
    padding: 0;
    width: 927px;
    height: 1200px;
    overflow: hidden;
    background: var(--ink);
  }
  .cover {
    position: relative;
    width: 927px;
    height: 1200px;
    overflow: hidden;
  }
  .cover__painting {
    position: absolute;
    inset: 0;
    display: block;
  }
  .cover__author-first {
    position: absolute;
    top: 22px;
    left: 0;
    width: 927px;
    margin: 0;
    text-align: center;
    font-family: "Anton", sans-serif;
    font-size: 160px;
    line-height: 1;
    letter-spacing: -2px;
    color: #14101c;
    -webkit-text-stroke: 3px var(--paper);
    text-transform: uppercase;
    transform: scaleX(0.93);
  }
  .cover__author-last {
    position: absolute;
    top: 236px;
    left: 0;
    width: 927px;
    margin: 0;
    text-align: center;
    font-family: "Anton", sans-serif;
    font-size: 132px;
    line-height: 1;
    letter-spacing: 30px;
    color: var(--paper);
    text-shadow: 3px 4px 4px rgba(0,0,0,0.45);
    text-transform: uppercase;
  }
  .cover__photo {
    position: absolute;
    left: 274px;
    top: 398px;
    width: 420px;
    height: 522px;
    background: var(--ink);
    display: flex;
    align-items: center;
    justify-content: center;
  }
  .cover__photo-label {
    font-family: "Roboto Condensed", sans-serif;
    font-weight: 300;
    font-size: 56px;
    color: var(--photo-label);
    margin-top: -30px;
  }
  .cover__title {
    position: absolute;
    top: 1022px;
    left: 0;
    width: 927px;
    margin: 0;
    text-align: center;
    font-family: "Roboto Condensed", sans-serif;
    font-weight: 300;
    font-size: 56px;
    line-height: 1;
    color: var(--paper);
    text-transform: uppercase;
  }
  .cover__publisher {
    position: absolute;
    top: 1096px;
    left: 0;
    width: 927px;
    margin: 0;
    text-align: center;
    font-family: "Roboto Condensed", sans-serif;
    font-weight: 700;
    font-size: 38px;
    line-height: 1;
    color: var(--paper);
    text-transform: uppercase;
  }
</style>
</head>
<body>
<main class="cover">
  <svg class="cover__painting" width="927" height="1200" viewBox="0 0 927 1200" role="img" aria-label="Abstract oil painting with thick brushstrokes in yellow, green, orange, red and blue">
    <defs>
      <linearGradient id="bottom-fade" x1="0" y1="0" x2="0" y2="1">
        <stop offset="0.6" stop-color="#000" stop-opacity="0"/>
        <stop offset="0.85" stop-color="#000" stop-opacity="0.75"/>
        <stop offset="1" stop-color="#000" stop-opacity="0.95"/>
      </linearGradient>
    </defs>
    <rect width="927" height="1200" fill="#3b2a2a"/>
    <rect x="0" y="0" width="220" height="420" fill="#5a3a2e"/>
    <rect x="0" y="400" width="210" height="300" fill="var(--paint-orange)"/>
    <rect x="0" y="700" width="220" height="260" fill="var(--paint-green)"/>
    <rect x="200" y="0" width="180" height="620" fill="var(--paint-yellow)"/>
    <rect x="360" y="0" width="400" height="520" fill="var(--paint-green)"/>
    <rect x="740" y="0" width="187" height="560" fill="var(--paint-sky)"/>
    <rect x="720" y="560" width="207" height="120" fill="var(--paint-blue)"/>
    <rect x="680" y="640" width="247" height="340" fill="var(--paint-orange)"/>
    <rect x="850" y="700" width="77" height="200" fill="var(--paint-red)"/>
    <rect x="200" y="620" width="80" height="320" fill="var(--paint-sky)"/>
    <rect width="927" height="1200" fill="url(#bottom-fade)"/>
  </svg>

  <h1 class="cover__author-first">Mireille</h1>
  <p class="cover__author-last">Fontaz</p>

  <div class="cover__photo" role="img" aria-label="Author photograph Quiet Harbor IV">
    <span class="cover__photo-label">PHOTO</span>
  </div>

  <h2 class="cover__title">Rain before the harvest</h2>
  <p class="cover__publisher">Marrow Editions</p>
</main>
</body>
</html>
```